Business Card Design Project

I need a business card design for a new business called Tolland Insurance Services. I am a small insurance broker that will provide business insurance services mostly to contractors and small businesses. My business is all about customer service and assistance rather than being a price driven/focused business. I want my business card to be professional giving the impression that I am larger than one person but not a corporate company. I have attached a copy of my logo.
Updates

Hi all

I have been advised that I need to show the following info for compliance reasons on my card. It only has to be small.

Can you please include either front or back:

Tolland Insurance Services Pty Ltd [ABN 61827405193] AR No 586714 as Authorised Representative of Brackford Insurance Group Pty Ltd ACN 274 906 518 ABN 82 274 906 518 AFS Licence No 718264

Reason: I need a further change to be made to the design. I need the contact number of 1300476815 added to the business card.

Hi All

I need one last change made to the card.

Can you please include the phone number 1300476815 to the card. If possible can this be made fairly clear on the card, either large on the back or another design idea you may have.

Target Market(s)

30+ Professionals

Industry/Entity Type

Insurance

Requirements
Must have
• I want a double sided design. My details to go on the card are as follows:

Dylan Tolland QRPSUV (Snr Assoc.) CIP
Director
PO Box 872, Kestrelvale SA 5091
Phone: 0438 617 204
Fax 08 8397 2418
Email: dylan@tollandinsure.example
Website: http://www.tollandinsure.example
Twitter: Tollandinsure
Facebook: facebook.com/tollandinsure

```html
<!DOCTYPE html>
<html lang="en">
<head>
<meta charset="utf-8">
<title>Tolland Insurance – Business Card</title>
<link href="https://fonts.googleapis.com/css2?family=Questrial&family=Arimo:wght@400;700&display=swap" rel="stylesheet">
<style>
  :root {
    --stage: #35312f;
    --card-front: #ffffff;
    --card-back: #e1e1e1;
    --ink: #1c1c1c;
    --ink-soft: #4a4a4a;
    --accent: #d4232a;
    --rule: #b9b9b9;
    --band: #2f2d2c;
    --band-text: #ffffff;
  }
  * { box-sizing: border-box; margin: 0; padding: 0; }
  html, body { width: 1200px; height: 846px; overflow: hidden; }
  body {
    background: var(--stage);
    position: relative;
    font-family: "Questrial", "Century Gothic", sans-serif;
    color: var(--ink);
  }
  .card {
    position: absolute;
    left: 169px;
    width: 508px;
    height: 290px;
    overflow: hidden;
  }
  .card--front { top: 106px; background: var(--card-front); }
  .card--back { top: 461px; background: var(--card-back); }

  /* Front */
  .slogan {
    position: absolute; left: 37px; top: 46px;
    font-size: 24px; line-height: 32px; color: var(--ink);
  }
  .slogan__key { color: var(--accent); font-size: 33px; line-height: 38px; display: block; }
  .brand-mini {
    position: absolute; right: 30px; top: 44px;
    display: flex; align-items: center; gap: 6px;
    font-size: 14px; color: var(--ink);
  }
  .brand-mini__dot { width: 8px; height: 8px; border-radius: 50%; background: var(--accent); }
  .person { position: absolute; right: 30px; top: 118px; text-align: right; }
  .person__name { font-size: 22px; line-height: 26px; }
  .person__role { font-family: "Arimo", Arial, sans-serif; font-size: 12.5px; line-height: 18px; color: var(--ink-soft); letter-spacing: 0.4px; }
  .card__rule { position: absolute; left: 37px; right: 30px; top: 193px; height: 2px; background: var(--rule); }
  .links, .contact {
    position: absolute; top: 205px;
    font-family: "Arimo", Arial, sans-serif; font-size: 10.5px; line-height: 18.5px; color: var(--ink-soft);
  }
  .links { left: 41px; }
  .links li { list-style: none; display: flex; align-items: center; gap: 8px; }
  .links__mark { width: 11px; height: 11px; background: var(--ink-soft); border-radius: 1px; }
  .links__globe { width: 11px; height: 11px; }
  .contact { right: 30px; text-align: right; letter-spacing: 0.9px; }

  /* Back */
  .brand {
    position: absolute; left: 36px; top: 109px;
    display: flex; align-items: center; gap: 10px;
    font-size: 22px; color: var(--ink);
  }
  .brand__dot { width: 12px; height: 12px; border-radius: 50%; background: var(--accent); }
  .hotline { position: absolute; left: 309px; top: 113px; width: 199px; height: 32px; }
  .hotline__band {
    position: absolute; left: 16px; top: 4px; right: 0; height: 25px;
    background: var(--band); border-radius: 6px 0 0 6px;
    color: var(--band-text); font-family: "Arimo", Arial, sans-serif; font-weight: 700;
    font-size: 16px; line-height: 25px; padding-left: 32px; letter-spacing: 1px;
  }
  .hotline__icon { position: absolute; left: 0; top: 0; width: 32px; height: 32px; }
  .legal__rule { position: absolute; left: 30px; right: 30px; top: 237px; height: 1px; background: var(--rule); }
  .legal {
    position: absolute; left: 20px; right: 20px; top: 244px;
    text-align: center; font-family: "Arimo", Arial, sans-serif; font-size: 7.4px; line-height: 10.5px; color: #6b6b6b;
  }
</style>
</head>
<body>

<section class="card card--front" aria-label="Business card front">
  <p class="slogan">Insurance<br>Advice<br>You Can<span class="slogan__key">Trust</span></p>
  <div class="brand-mini"><span class="brand-mini__dot"></span>Tolland Insurance</div>
  <div class="person">
    <p class="person__name">Dylan Tolland</p>
    <p class="person__role">QRPSUV (Snr Assoc.) CIP</p>
    <p class="person__role">Director</p>
  </div>
  <div class="card__rule"></div>
  <ul class="links">
    <li><span class="links__mark"></span>Tollandinsure</li>
    <li><span class="links__mark"></span>tollandinsure</li>
    <li>
      <svg class="links__globe" viewBox="0 0 12 12" aria-hidden="true">
        <g fill="none" stroke="#4a4a4a" stroke-width="1">
          <circle cx="6" cy="6" r="5.2"/><ellipse cx="6" cy="6" rx="2.3" ry="5.2"/><line x1="0.8" y1="6" x2="11.2" y2="6"/>
        </g>
      </svg>www.tollandinsure.example
    </li>
  </ul>
  <div class="contact">
    <p>dylan@tollandinsure.example</p>
    <p>TEL: 0438 617 204</p>
    <p>FAX: 08 8397 2418</p>
  </div>
</section>

<section class="card card--back" aria-label="Business card back">
  <div class="brand"><span class="brand__dot"></span>Tolland Insurance</div>
  <div class="hotline">
    <div class="hotline__band">1300 476 815</div>
    <svg class="hotline__icon" viewBox="0 0 32 32" aria-hidden="true">
      <circle cx="16" cy="16" r="15" fill="#d4232a" stroke="#ffffff" stroke-width="1.5"/>
      <path d="M11 9.5c1-.8 2-.6 2.6.4l1.3 2.3c.5.9.2 1.8-.6 2.3l-.8.5c.7 1.9 2 3.3 3.8 4.2l.6-.8c.6-.8 1.5-1 2.3-.5l2.2 1.4c1 .6 1.1 1.7.3 2.6-1.3 1.4-3 1.8-4.8 1-3.8-1.7-6.6-4.8-7.9-8.7-.5-1.8 0-3.5 1-4.7z" fill="#ffffff"/>
    </svg>
  </div>
  <div class="legal__rule"></div>
  <p class="legal">Tolland Insurance Services Pty Ltd [ABN 61827405193] AR No 586714 as Authorised Representative<br>of Brackford Insurance Group Pty Ltd ACN 274 906 518 ABN 82 274 906 518 AFS Licence No 718264</p>
</section>

</body>
</html>
```